Telecommunications/Power civil contractor needs business card design

Were a new telecommunications/power underground civil contractor that is looking for a new business card design. Our company colours are silver or grey and orange. Feel free to use the white background logo or the black background logo.

Target Market(s)

Local contractors, utility companies, private sector mining/energy companies, developers.

Industry/Entity Type

Telecommunications

Contact Information for Business Card

Each card will need the following info:
Persons name:
Title:
E-mail:
Phone number:
Shop Address:
Mailing Address:

Requirements
Must have
• Each card will need the following info:
• Persons name:
• Title:
• E-mail:
• Phone number:
• Shop Address:
• Mailing Address:

```html
<!DOCTYPE html>
<html lang="en">
<head>
<meta charset="utf-8">
<title>Tandem Line Contracting Inc – Business Card</title>
<link rel="stylesheet" href="https://fonts.googleapis.com/css2?family=Arimo:ital,wght@0,400;0,700;1,400&display=swap">
<style>
  :root {
    --canvas: #d9d9d9;
    --card-grey: #676869;
    --card-white: #ececec;
    --silver-light: #ffffff;
    --silver-dark: #a9a9ab;
    --ink-dark: #2f2f30;
    --ink-grey: #6a6b6c;
    --orange: #f15a22;
  }
  * { box-sizing: border-box; margin: 0; padding: 0; }
  html, body {
    width: 1200px; height: 864px; overflow: hidden;
    background: var(--canvas);
    font-family: "Arimo", Arial, sans-serif;
  }
  .sheet {
    position: relative; width: 1200px; height: 864px;
    display: flex; flex-direction: column; align-items: center;
    gap: 16px; padding-top: 24px;
  }
  .card {
    position: relative; width: 700px; height: 400px;
    box-shadow: 0 4px 14px rgba(0,0,0,.18);
    overflow: hidden;
  }
  .card-bg { position: absolute; inset: 0; width: 100%; height: 100%; }

  /* Back side */
  .back-mark {
    position: absolute; left: 95px; top: 105px; width: 190px; height: 190px;
  }
  .back-name {
    position: absolute; left: 425px; top: 135px; width: 255px;
    color: var(--ink-grey); font-weight: 700; text-transform: uppercase;
    line-height: 1.05; letter-spacing: 1px;
  }
  .back-name .line-main { display: block; font-size: 44px; }
  .back-name .line-sub { display: block; font-size: 20px; margin-top: 14px; letter-spacing: 1.5px; }

  /* Front side */
  .person { position: absolute; left: 70px; top: 52px; color: var(--ink-dark); }
  .person-name { font-size: 31px; font-weight: 400; }
  .person-title { font-size: 19px; font-style: italic; margin-top: 2px; }
  .address {
    position: absolute; left: 62px; top: 152px; font-style: normal;
    color: var(--ink-dark); font-size: 17px; line-height: 20px;
  }
  .contacts {
    position: absolute; left: 56px; top: 222px; list-style: none;
    color: var(--ink-dark); font-size: 17px;
  }
  .contacts li { display: flex; align-items: center; gap: 10px; height: 24px; }
  .contacts svg { width: 16px; height: 16px; flex: none; }

  .brand {
    position: absolute; left: 440px; top: 95px; width: 240px;
    display: flex; flex-direction: column; align-items: center;
  }
  .brand-dot {
    width: 110px; height: 110px; border-radius: 50%;
    border: 7px solid var(--orange); margin-bottom: 22px;
  }
  .brand-name {
    color: var(--ink-grey); font-weight: 700; text-transform: uppercase;
    text-align: center; line-height: 1.1; white-space: nowrap;
  }
  .brand-name .line-main { display: block; font-size: 30px; letter-spacing: 1px; }
  .brand-name .line-sub { display: block; font-size: 18px; letter-spacing: 1px; margin-top: 2px; }
</style>
</head>
<body>
<main class="sheet">

  <section class="card card-back" aria-label="Business card back">
    <svg class="card-bg" viewBox="0 0 700 400" preserveAspectRatio="none">
      <defs>
        <linearGradient id="silverBack" x1="0" y1="0" x2="0" y2="1">
          <stop offset="0" stop-color="var(--silver-dark)"/>
          <stop offset=".5" stop-color="var(--silver-light)"/>
          <stop offset="1" stop-color="var(--silver-dark)"/>
        </linearGradient>
      </defs>
      <rect width="700" height="400" fill="var(--card-white)"/>
      <path d="M0 0 H400 C 370 120, 360 260, 385 400 H0 Z" fill="url(#silverBack)"/>
      <path d="M0 0 H388 C 358 120, 348 260, 373 400 H0 Z" fill="var(--card-grey)"/>
    </svg>
    <svg class="back-mark" viewBox="0 0 190 190" aria-hidden="true">
      <circle cx="95" cy="95" r="88" fill="none" stroke="#5a5b5c" stroke-width="3"/>
    </svg>
    <p class="back-name">
      <span class="line-main">Tandem</span>
      <span class="line-main">Line</span>
      <span class="line-sub">Contracting Inc</span>
    </p>
  </section>

  <section class="card card-front" aria-label="Business card front">
    <svg class="card-bg" viewBox="0 0 700 400" preserveAspectRatio="none">
      <defs>
        <linearGradient id="silverFront" x1="0" y1="0" x2="1" y2="1">
          <stop offset="0" stop-color="var(--silver-dark)"/>
          <stop offset=".5" stop-color="var(--silver-light)"/>
          <stop offset="1" stop-color="var(--silver-dark)"/>
        </linearGradient>
      </defs>
      <rect width="700" height="400" fill="var(--card-white)"/>
      <path d="M0 0 H488 C 390 90, 320 250, 280 400 H0 Z" fill="url(#silverFront)"/>
      <path d="M0 0 H474 C 376 90, 306 250, 266 400 H0 Z" fill="var(--card-grey)"/>
    </svg>

    <div class="person">
      <h1 class="person-name">Alex Morgan</h1>
      <p class="person-title">General Manager</p>
    </div>

    <address class="address">
      Street Address,&nbsp; Suite 00<br>
      Statename 00000
    </address>

    <ul class="contacts">
      <li>
        <svg viewBox="0 0 16 16" aria-hidden="true"><rect x="3" y="1" width="10" height="14" rx="2" fill="var(--ink-dark)"/><rect x="5" y="3" width="6" height="8" fill="var(--card-grey)"/></svg>
        555 0142 2381
      </li>
      <li>
        <svg viewBox="0 0 16 16" aria-hidden="true"><circle cx="8" cy="8" r="8" fill="var(--ink-dark)"/><path d="M5 4 L7 4 L7.5 6 L6.5 7 C7 8.5 7.5 9 9 9.5 L10 8.5 L12 9 L12 11 C8 11.5 4.5 8 5 4Z" fill="var(--card-grey)"/></svg>
        555 0178 4420
      </li>
      <li>
        <svg viewBox="0 0 16 16" aria-hidden="true"><circle cx="8" cy="8" r="8" fill="var(--ink-dark)"/><rect x="3.5" y="5" width="9" height="6" fill="var(--card-grey)"/><path d="M3.5 5 L8 8.5 L12.5 5" fill="none" stroke="var(--ink-dark)" stroke-width="1"/></svg>
        info@tandemlinecivil.com
      </li>
      <li>
        <svg viewBox="0 0 16 16" aria-hidden="true"><circle cx="8" cy="8" r="8" fill="var(--ink-dark)"/><g fill="none" stroke="var(--card-grey)" stroke-width="1"><circle cx="8" cy="8" r="5"/><ellipse cx="8" cy="8" rx="2.2" ry="5"/><path d="M3 8 H13"/></g></svg>
        www.tandemlinecivil.com
      </li>
    </ul>

    <div class="brand">
      <span class="brand-dot" aria-hidden="true"></span>
      <p class="brand-name">
        <span class="line-main">Tandem Line</span>
        <span class="line-sub">Contracting Inc</span>
      </p>
    </div>
  </section>

</main>
</body>
</html>
```